Bed Company needs business card

Hello, we are a bed company that makes specialized magnets for beds. We are an alternative healing company. I need a modern and upscale business card. Please incorporate my logo for the card.

Accepted file formats are AI, EPS, and Press-Ready PDFS.

Please include all fonts or convert them to outlines regardless of file type.

If you are designing the card in Photoshop the file Must be 1200dpi.

I am open to anything for the business card.  I really like all of your designs and if you want to change the color of the logo, you can.  I will be making the final selection by Friday.  Thank You for all of your designs.  Feel Free to submit different color logos if you want.  

Reason: I will make a decision Final on Friday April 20th. 2012. Good Luck and Thank you all for the designs.

Target Market(s)

My target Market is people, who are looking for alternative healing.

Industry/Entity Type

Business

Requirements
Must have
• My logo must be incorporated. The front card must have

Name
Job Title

Address
Work
Cell
Fax
email
web

Just put in fake info for the card.

The back of the card. I want the logo on the back with color. I just want it to look modern and cool.

```html
<!DOCTYPE html>
<html lang="en">
<head>
<meta charset="utf-8">
<title>Lodestone Rest – Business Card</title>
<link rel="stylesheet" href="https://fonts.googleapis.com/css2?family=Noto+Sans:wght@400;700&display=swap">
<style>
  :root {
    --stage: #55504f;
    --paper: #ffffff;
    --brand-navy: #2a4572;
    --band-top: #0a1a95;
    --band-top-edge: #061680;
    --band-bottom: #080f6e;
    --band-bottom-edge: #050c5c;
    --ink-light: #ffffff;
  }
  * { margin: 0; padding: 0; box-sizing: border-box; }
  html, body {
    width: 1200px; height: 988px; overflow: hidden;
    background: var(--stage);
    font-family: "Noto Sans", Verdana, sans-serif;
  }
  .canvas { position: relative; width: 1200px; height: 988px; }

  .card { position: absolute; width: 618px; height: 353px; overflow: hidden; }

  /* Logo side */
  .card-back { left: 109px; top: 94px; background: var(--paper); }
  .edge-pattern {
    position: absolute; left: 4px; right: 4px; height: 26px;
    background: var(--brand-navy);
  }
  .edge-pattern-top { top: 2px; }
  .edge-pattern-bottom { bottom: 3px; }
  .brand {
    position: absolute; right: 166px; top: 146px;
    text-align: right; color: var(--brand-navy);
  }
  .brand-name { font-size: 36px; font-weight: 700; letter-spacing: -0.5px; line-height: 1.2; }
  .brand-tagline { font-size: 16px; font-weight: 400; margin-top: 4px; letter-spacing: 0.3px; }

  /* Details side */
  .card-front { left: 460px; top: 471px; color: var(--ink-light); font-weight: 700; }
  .name-band {
    position: absolute; left: 0; top: 0; width: 100%; height: 135px;
    background: linear-gradient(180deg, var(--band-top-edge), var(--band-top) 50%, var(--band-top-edge));
  }
  .divider { position: absolute; left: 0; top: 135px; width: 100%; height: 7px; background: var(--paper); }
  .contact-band {
    position: absolute; left: 0; top: 142px; width: 100%; height: 211px;
    background: linear-gradient(180deg, var(--band-bottom-edge), var(--band-bottom) 50%, var(--band-bottom-edge));
  }
  .person-name { position: absolute; left: 262px; top: 26px; font-size: 21px; letter-spacing: 0.5px; line-height: 1.3; }
  .person-title { position: absolute; left: 319px; top: 56px; font-size: 10.8px; letter-spacing: 0.2px; line-height: 1.3; }
  .contact-list { position: absolute; left: 343px; top: 166px; list-style: none; font-size: 14px; }
  .contact-list li { height: 28.6px; line-height: 18px; }
  .online { position: absolute; left: 128px; top: 298px; width: 270px; text-align: center; font-size: 13px; }
  .online p { line-height: 22px; }
</style>
</head>
<body>
<main class="canvas">
  <section class="card card-back">
    <div class="edge-pattern edge-pattern-top" role="img" aria-label="Navy wave pattern border along the top edge"></div>
    <div class="brand">
      <p class="brand-name">Lodestone Rest</p>
      <p class="brand-tagline">Alternative Healing</p>
    </div>
    <div class="edge-pattern edge-pattern-bottom" role="img" aria-label="Navy wave pattern border along the bottom edge"></div>
  </section>

  <section class="card card-front">
    <div class="name-band"></div>
    <div class="divider"></div>
    <div class="contact-band"></div>
    <h1 class="person-name">DANIEL BROOKS</h1>
    <p class="person-title">MANAGING DIRECTOR</p>
    <ul class="contact-list">
      <li>ADD:HARBOR SQUARE</li>
      <li>WORK: ALTERNATIVE BED HEALING</li>
      <li>CELL:071548392</li>
      <li>FAX:004617205</li>
    </ul>
    <div class="online">
      <p>daniel@restmail.com</p>
      <p>www.lodestonerest.com</p>
    </div>
  </section>
</main>
</body>
</html>
```